Puslishing House Needs poster Design for Medical Book

We need an advertisement desing for a medical book on cardiology named "Vertentes" (Hypertension), which 2nd Edition we launched last August. What makes this book special is that this is the first time in history that a hypertension book has a second edition in Brazil and was written by the Vascular Unit of the Southern Clinical Guild of Heart Studies in comemoration in its 100 years. The two news about this book is that we sold 1000 units since we launched (which is good) and we have now an ebook version for all tablet, smartphones and readers. From this month on it is going to happen importants hypertension meetings and we want to promote this two news about this book - 1000 units sold and ebook version. We would like to see designs that use orange (the publishing house color) and communicate celebration.

Target Market(s)

Doctors Specialist from several segments like Cardiology, Endocrinology, Nephrology, Nutrition. Most of the target are man with 50 years-old.

Industry/Entity Type

Medical

Requirements
Must have
• The adverstisement must have the attached book cover and publishing house logo (Marlowan) using only the name (without the tree) or the complete logo.
Should not have
• The design should not use old-style, serif fonts like Times new Roman.

```html
<!DOCTYPE html>
<html lang="en">
<head>
<meta charset="utf-8">
<title>Vertentes – 2nd Edition Poster</title>
<link rel="stylesheet" href="https://fonts.googleapis.com/css2?family=Oswald:wght@500;600&family=Montserrat:wght@700;800&display=swap">
<style>
  :root {
    --poster-orange: #cf401c;
    --band-green-dark: #06320e;
    --band-green: #0f6424;
    --band-green-light: #3d8a3a;
    --text-white: #ffffff;
    --cover-pale: #e9ecea;
    --cover-green: #2f5a3c;
    --badge-blue: #3f5f9c;
  }
  * { margin: 0; padding: 0; box-sizing: border-box; }
  html, body { width: 863px; height: 1200px; overflow: hidden; }
  body { background: var(--poster-orange); }
  .poster {
    position: relative;
    width: 863px;
    height: 1200px;
    background: var(--poster-orange);
    color: var(--text-white);
    overflow: hidden;
  }
  .poster__kicker {
    position: absolute;
    top: 30px; left: 0; width: 100%;
    text-align: center;
    font-family: "Oswald", sans-serif;
    font-weight: 500;
    font-size: 17px;
    letter-spacing: 0.2px;
  }
  .poster__band {
    position: absolute;
    top: 110px; left: 0;
    width: 863px; height: 470px;
  }
  .poster__title {
    position: absolute;
    top: 265px; left: 0; width: 100%;
    text-align: center;
    font-family: "Oswald", sans-serif;
    font-weight: 600;
    font-size: 150px;
    line-height: 1;
    letter-spacing: 1px;
    text-shadow: 0 3px 6px rgba(0,0,0,0.35);
  }
  .news {
    position: absolute;
    left: 54px;
    font-family: "Montserrat", sans-serif;
    font-weight: 800;
    text-shadow: 0 2px 4px rgba(0,0,0,0.3);
  }
  .news--sales { top: 618px; }
  .news--ebook { top: 735px; }
  .news__headline { font-size: 38px; line-height: 1.05; letter-spacing: 0.3px; }
  .news__detail { font-weight: 700; font-size: 25px; line-height: 1.2; margin-top: 4px; }
  .book-cover {
    position: absolute;
    left: 380px; top: 610px;
    width: 460px; height: 560px;
  }
  .publisher-name {
    position: absolute;
    left: 44px; top: 1110px;
    font-family: "Montserrat", sans-serif;
    font-weight: 700;
    font-size: 22px;
  }
  .partner-badge {
    position: absolute;
    left: 164px; top: 1096px;
    width: 56px; height: 56px;
    border-radius: 50%;
    background: var(--badge-blue);
  }
  .department-name {
    position: absolute;
    left: 236px; top: 1104px;
    width: 180px;
    font-family: "Montserrat", sans-serif;
    font-weight: 700;
    font-size: 11px;
    line-height: 1.3;
    text-transform: uppercase;
  }
  .publisher-web {
    position: absolute;
    right: 42px; top: 1152px;
    font-family: "Montserrat", sans-serif;
    font-weight: 700;
    font-size: 12px;
  }
</style>
</head>
<body>
<main class="poster">
  <p class="poster__kicker">FIRST TIME IN HISTORY THAT A HYPERTENSION BOOK HAS A SECOND EDITION IN BRAZIL</p>

  <svg class="poster__band" viewBox="0 0 863 470" aria-hidden="true">
    <defs>
      <radialGradient id="bandGlow" cx="0.55" cy="0.45" r="0.7">
        <stop offset="0" stop-color="#3d8a3a"/>
        <stop offset="0.45" stop-color="#0f6424"/>
        <stop offset="1" stop-color="#06320e"/>
      </radialGradient>
    </defs>
    <path d="M0 110 C 260 40, 560 10, 863 20 L 863 330 C 600 360, 300 420, 0 470 Z" fill="url(#bandGlow)"/>
  </svg>

  <h1 class="poster__title">VERTENTES</h1>

  <section class="news news--sales">
    <h2 class="news__headline">1000 UNITS SOLD</h2>
    <p class="news__detail">Since launched</p>
  </section>

  <section class="news news--ebook">
    <h2 class="news__headline">EBOOK VERSION</h2>
    <p class="news__detail">now an ebook version<br>is available for all<br>tablet, smartphones<br>and readers</p>
  </section>

  <svg class="book-cover" viewBox="0 0 460 560" role="img" aria-label="Photo of the Vertentes 2nd edition book cover, standing on a second copy lying flat">
    <defs>
      <linearGradient id="coverTone" x1="0" y1="0" x2="0" y2="1">
        <stop offset="0" stop-color="#2f5a3c"/>
        <stop offset="0.35" stop-color="#e9ecea"/>
        <stop offset="1" stop-color="#cfd6d2"/>
      </linearGradient>
      <linearGradient id="baseTone" x1="0" y1="0" x2="1" y2="1">
        <stop offset="0" stop-color="#5c7a62"/>
        <stop offset="0.5" stop-color="#dfe4e1"/>
        <stop offset="1" stop-color="#f4f6f5"/>
      </linearGradient>
    </defs>
    <polygon points="20,380 380,375 452,460 90,555" fill="url(#baseTone)"/>
    <rect x="69" y="10" width="299" height="388" fill="url(#coverTone)"/>
  </svg>

  <span class="publisher-name">Marlowan</span>
  <span class="partner-badge" aria-hidden="true"></span>
  <span class="department-name">Vascular Unit of the Southern Clinical Guild of Heart Studies</span>
  <p class="publisher-web">www.marlowan.com.br</p>
</main>
</body>
</html>
```